Lanternwick Pathway Ledger Basics

size of the ad - 8”x 10.75" plus 0.25" bleed
I would like an ad for a magazine that will stand out and make people want to read the ad.
The ad should not be crowded and people reading the ad will be able to read the text.
I would like it to be a creative and modern-day design.
the list of topics should not be the focus of the ad.
the text is attached.
If you decide to use people in the ad then please no ladies.
please note that leave over 1 inch for the bottom of the footer

```html
<!DOCTYPE html>
<html lang="en">
<head>
<meta charset="utf-8">
<title>Lanternwick Pathway Ledger Basics – Course Ad</title>
<link rel="stylesheet" href="https://fonts.googleapis.com/css2?family=Oswald:wght@700&family=Inter:ital,wght@0,300;0,400;0,700;1,300;1,800&display=swap">
<style>
  :root {
    --sky-top: #5d6163;
    --sky-mid: #8a8e90;
    --city-dark: #2a2c2d;
    --city-mid: #4a4d4f;
    --panel: rgba(28, 28, 28, 0.84);
    --white: #ffffff;
    --soft-white: #e9e9e9;
    --muted: #c9c9c9;
    --rule: rgba(255, 255, 255, 0.7);
  }
  * { margin: 0; padding: 0; box-sizing: border-box; }
  html, body { width: 893px; height: 1200px; overflow: hidden; background: #fff; }
  .ad {
    position: relative;
    width: 893px;
    height: 1200px;
    overflow: hidden;
    font-family: "Inter", Helvetica, Arial, sans-serif;
    color: var(--white);
  }
  .ad__photo {
    position: absolute;
    inset: 0;
    background:
      linear-gradient(90deg, rgba(120,115,100,0.35) 0%, rgba(0,0,0,0) 22%),
      linear-gradient(180deg, var(--sky-top) 0%, var(--sky-mid) 9%, var(--city-mid) 30%, var(--city-dark) 60%, #6e7170 88%, #9a9c98 100%);
  }
  .ad__masthead {
    position: absolute;
    top: -22px;
    left: 50%;
    transform: translateX(-50%);
    white-space: nowrap;
    font-family: "Oswald", "Arial Narrow", sans-serif;
    font-weight: 700;
    font-size: 118px;
    line-height: 1;
    letter-spacing: 1px;
    color: var(--white);
    text-shadow: 0 2px 3px rgba(0,0,0,0.25);
  }
  .ad__panel {
    position: absolute;
    left: 163px;
    top: 124px;
    width: 730px;
    height: 974px;
    background: var(--panel);
  }
  .course-title {
    position: absolute;
    left: 205px;
    top: 164px;
    font-weight: 700;
    font-size: 45px;
    line-height: 54px;
    text-transform: uppercase;
    letter-spacing: 0.3px;
  }
  .tagline {
    position: absolute;
    left: 204px;
    top: 288px;
    font-style: italic;
    font-weight: 300;
    font-size: 29px;
    line-height: 45px;
    letter-spacing: 3.6px;
    text-transform: uppercase;
    color: var(--soft-white);
  }
  .location {
    position: absolute;
    left: 215px;
    top: 421px;
    font-weight: 700;
    font-size: 33px;
    line-height: 40px;
  }
  .location-rule {
    position: absolute;
    left: 204px;
    top: 472px;
    width: 399px;
    height: 1px;
    background: var(--rule);
  }
  .details {
    position: absolute;
    left: 215px;
    top: 479px;
    list-style: none;
    font-weight: 700;
    font-size: 23.5px;
    line-height: 37px;
  }
  .offer {
    position: absolute;
    left: 215px;
    top: 627px;
  }
  .offer__label {
    font-style: italic;
    font-weight: 800;
    font-size: 21px;
    line-height: 28px;
    color: var(--muted);
  }
  .offer__note {
    font-weight: 300;
    font-size: 21px;
    line-height: 28px;
    color: var(--soft-white);
  }
  .topics {
    position: absolute;
    left: 215px;
    top: 746px;
  }
  .topics__heading {
    font-weight: 700;
    font-size: 20px;
    line-height: 28px;
  }
  .topics__list {
    list-style: none;
    font-weight: 400;
    font-size: 20px;
    line-height: 28px;
    color: var(--soft-white);
  }
</style>
</head>
<body>
  <main class="ad">
    <div class="ad__photo" role="img" aria-label="Photograph of modern glass-and-concrete office buildings along a tree-lined pedestrian street under a cloudy grey sky"></div>

    <div class="ad__masthead">REAL ESTATE COURSE</div>

    <section class="ad__panel" aria-hidden="false"></section>

    <h1 class="course-title">Lanternwick Pathway<br>Ledger Basics</h1>

    <p class="tagline">Investing in knowledge is<br>investing in opportunities.</p>

    <h2 class="location">Brookhollow</h2>
    <div class="location-rule"></div>

    <ul class="details">
      <li>10 -Tuesday evenings sessions</li>
      <li>Starting Feb.28</li>
      <li>Limited Partial Scholarships</li>
    </ul>

    <div class="offer">
      <p class="offer__label">Early Bird Special</p>
      <p class="offer__note">For those that started or would like to go into real estate</p>
    </div>

    <div class="topics">
      <p class="topics__heading">Topics: partial listing</p>
      <ul class="topics__list">
        <li>Real estate investment strategies</li>
        <li>Due diligence</li>
        <li>Financing</li>
        <li>Underwriting</li>
        <li>Property management</li>
        <li>Real estate Legal basics</li>
        <li>Sourcing deals</li>
        <li>Syndication</li>
        <li>Dealing with brokers</li>
        <li>Tax fundamentals</li>
      </ul>
    </div>
  </main>
</body>
</html>
```